Flyer design for the Harvest Lantern Summit 2019 (HALSUM)

Design a flyer for our annual conference with basic information about the conference: conference logo and year, Conference name: Harvest Lantern Summit Location: Talbot Community Center (Downtown Portland)482 Wexley Street, Portland, ME 04109, Date: August 8th, 9th, 10th and 11th, 2019Start time 7:00PMI would like the following three words added to the flyer. These words describe the vision of the conference: Prophetic, Fire, Overflow,

Contact info:
Website: www.vostel.org
Phone: 207 555 3184
Email: contact@meadowcrest.org

Target Market(s)

Young adults living in the United States

Industry/Entity Type

Religious

Font styles to use
Sans Serif

Colors

Designer to choose colors to be used in the design.

Requirements
Must have
• HALSUM must logo standout, the reader should be able to take a quick look and find key info,
Should not have
• Cross image, church image

```html
<!DOCTYPE html>
<html lang="en">
<head>
<meta charset="utf-8">
<title>Harvest Lantern Summit 2019</title>
<link rel="stylesheet" href="https://fonts.googleapis.com/css2?family=Anton&family=Montserrat:wght@500;600;700;800&display=swap">
<style>
  :root {
    --orange: #f08c1e;
    --blue: #1673bb;
    --ink: #2a2a2a;
    --paper: #ffffff;
    --faint: #ececec;
    --rule: #8a8a8a;
  }
  * { margin: 0; padding: 0; box-sizing: border-box; }
  html, body { width: 903px; height: 1200px; overflow: hidden; background: var(--paper); }
  .flyer {
    position: relative; width: 903px; height: 1200px; overflow: hidden;
    background: radial-gradient(ellipse at 80% 10%, #f7f7f7 0%, var(--paper) 60%);
    font-family: "Montserrat", sans-serif;
  }
  .year-watermark {
    position: absolute; left: 826px; top: 410px; width: 90px;
    font-family: "Anton", sans-serif; font-size: 170px; line-height: 172px;
    color: var(--faint); text-align: center;
  }
  .brand { position: absolute; top: 62px; left: 0; width: 903px; text-align: center; }
  .brand-name {
    display: inline-flex; align-items: center; gap: 14px;
    font-family: "Montserrat", sans-serif; font-weight: 800; font-size: 62px;
    color: var(--blue); letter-spacing: 1px; line-height: 1;
  }
  .brand-dot { width: 22px; height: 22px; border-radius: 50%; background: var(--orange); }
  .brand-year {
    display: flex; align-items: center; justify-content: center; gap: 14px;
    margin-top: 12px; color: var(--orange); font-weight: 700; font-size: 34px; letter-spacing: 20px;
  }
  .brand-year::before, .brand-year::after { content: ""; width: 100px; height: 2px; background: var(--orange); }
  .title {
    position: absolute; top: 232px; left: 0; width: 903px; text-align: center;
    font-family: "Anton", sans-serif; font-size: 98px; line-height: 110px; text-transform: uppercase;
  }
  .title-top { color: var(--orange); display: block; }
  .title-bottom { color: var(--blue); display: block; }
  .flame-art {
    position: absolute; left: 0; top: 438px; width: 348px; height: 678px;
    background: linear-gradient(180deg, #f2a020 0%, #a99a6a 45%, #2f93c8 100%);
    border-radius: 0 100% 60% 0 / 0 70% 30% 0;
    opacity: .95;
  }
  .pillars { position: absolute; top: 483px; left: 0; width: 903px; }
  .pillar { position: absolute; width: 220px; margin-left: -110px; text-align: center; }
  .pillar svg { display: block; margin: 0 auto; }
  .pillar-label { margin-top: 14px; font-weight: 700; font-size: 33px; color: var(--ink); letter-spacing: .5px; }
  .details { position: absolute; left: 396px; top: 690px; width: 440px; }
  .detail-row { position: relative; padding-left: 80px; }
  .detail-icon { position: absolute; left: 0; top: 0; }
  .date-month { color: var(--orange); font-weight: 700; font-size: 40px; line-height: 46px; }
  .date-days { color: var(--blue); font-weight: 700; font-size: 37px; line-height: 47px; white-space: nowrap; }
  .rule { height: 1.5px; background: var(--rule); margin-left: 80px; }
  .rule-a { margin-top: 22px; }
  .time { margin-top: 22px; color: var(--orange); font-weight: 700; font-size: 28px; line-height: 36px; }
  .time strong { color: var(--blue); font-weight: 700; }
  .rule-b { margin-top: 18px; }
  .venue { margin-top: 22px; font-weight: 700; font-size: 26px; line-height: 33px; white-space: nowrap; }
  .venue-name { color: var(--orange); }
  .venue-address { color: var(--blue); }
  .contact-bar {
    position: absolute; left: 5px; top: 1116px; width: 886px; height: 66px;
    background: var(--blue); display: flex; align-items: center; justify-content: space-around;
    color: var(--paper); font-weight: 500; font-size: 21px;
  }
  .contact-item { display: flex; align-items: center; gap: 14px; }
  .contact-icon { width: 30px; height: 30px; border-radius: 50%; background: var(--paper); display: flex; align-items: center; justify-content: center; }
</style>
</head>
<body>
<main class="flyer">
  <div class="year-watermark" aria-hidden="true">2<br>0<br>1<br>9</div>
  <div class="flame-art" role="img" aria-label="Large stylised flame artwork in orange fading to blue"></div>

  <header class="brand">
    <div class="brand-name"><span class="brand-dot"></span>HALSUM</div>
    <div class="brand-year">2019</div>
  </header>

  <h1 class="title">
    <span class="title-top">Harvest Lantern</span>
    <span class="title-bottom">Summit</span>
  </h1>

  <section class="pillars">
    <div class="pillar" style="left:226px">
      <svg width="82" height="82" viewBox="0 0 82 82">
        <path d="M5 41 A36 36 0 0 1 77 41" fill="none" stroke="var(--orange)" stroke-width="5"/>
        <path d="M77 41 A36 36 0 0 1 5 41" fill="none" stroke="var(--ink)" stroke-width="5"/>
        <path d="M41 58 C30 50 26 42 30 34 C33 28 39 29 41 34 C43 29 49 28 52 34 C56 42 52 50 41 58Z" fill="var(--orange)"/>
      </svg>
      <div class="pillar-label">PROPHETIC</div>
    </div>
    <div class="pillar" style="left:451px">
      <svg width="82" height="82" viewBox="0 0 82 82">
        <path d="M5 41 A36 36 0 0 1 77 41" fill="none" stroke="var(--orange)" stroke-width="5"/>
        <path d="M77 41 A36 36 0 0 1 5 41" fill="none" stroke="var(--ink)" stroke-width="5"/>
        <path d="M41 20 C50 32 56 40 54 50 C52 58 46 62 41 62 C34 62 28 56 28 49 C28 42 34 38 36 30 C39 36 40 38 41 40 C44 34 44 27 41 20Z" fill="var(--orange)"/>
      </svg>
      <div class="pillar-label">FIRE</div>
    </div>
    <div class="pillar" style="left:674px">
      <svg width="82" height="82" viewBox="0 0 82 82">
        <path d="M5 41 A36 36 0 0 1 77 41" fill="none" stroke="var(--orange)" stroke-width="5"/>
        <path d="M77 41 A36 36 0 0 1 5 41" fill="none" stroke="var(--ink)" stroke-width="5"/>
        <g fill="none" stroke="var(--orange)" stroke-width="3.5" stroke-linecap="round">
          <path d="M25 32 Q29 28 33 32 T41 32 T49 32 T57 32"/>
          <path d="M25 42 Q29 38 33 42 T41 42 T49 42 T57 42"/>
          <path d="M25 52 Q29 48 33 52 T41 52 T49 52 T57 52"/>
        </g>
      </svg>
      <div class="pillar-label">OVERFLOW</div>
    </div>
  </section>

  <section class="details">
    <div class="detail-row">
      <svg class="detail-icon" width="48" height="50" viewBox="0 0 48 50" style="top:6px">
        <rect x="3" y="7" width="42" height="40" rx="3" fill="none" stroke="var(--orange)" stroke-width="3"/>
        <rect x="3" y="7" width="42" height="9" fill="var(--orange)"/>
        <rect x="12" y="2" width="4" height="10" fill="var(--orange)"/>
        <rect x="32" y="2" width="4" height="10" fill="var(--orange)"/>
        <g fill="var(--orange)">
          <rect x="10" y="22" width="6" height="5"/><rect x="19" y="22" width="6" height="5"/><rect x="28" y="22" width="6" height="5"/>
          <rect x="10" y="30" width="6" height="5"/><rect x="19" y="30" width="6" height="5"/><rect x="28" y="30" width="6" height="5"/>
          <rect x="10" y="38" width="6" height="5"/><rect x="19" y="38" width="6" height="5"/><rect x="28" y="38" width="6" height="5"/>
        </g>
      </svg>
      <div class="date-month">AUGUST</div>
      <div class="date-days">8th, 9th,<br>10th &amp; 11th, 2019</div>
    </div>
    <div class="rule rule-a"></div>
    <div class="detail-row time">
      <svg class="detail-icon" width="50" height="52" viewBox="0 0 50 52" style="top:-10px">
        <circle cx="25" cy="28" r="18" fill="none" stroke="var(--orange)" stroke-width="4"/>
        <path d="M25 18 V29 H33" fill="none" stroke="var(--orange)" stroke-width="3"/>
        <path d="M4 12 A9 9 0 0 1 15 4" fill="none" stroke="var(--orange)" stroke-width="4"/>
        <path d="M46 12 A9 9 0 0 0 35 4" fill="none" stroke="var(--orange)" stroke-width="4"/>
        <path d="M12 44 L8 50 M38 44 L42 50" stroke="var(--orange)" stroke-width="4"/>
      </svg>
      Start time <strong>7:00PM</strong>
    </div>
    <div class="rule rule-b"></div>
    <div class="detail-row venue">
      <svg class="detail-icon" width="44" height="52" viewBox="0 0 44 52" style="top:2px">
        <path d="M22 50 C10 36 4 28 4 20 A18 18 0 0 1 40 20 C40 28 34 36 22 50Z" fill="var(--orange)"/>
        <circle cx="22" cy="20" r="7" fill="var(--paper)"/>
      </svg>
      <div class="venue-name">Talbot Community Center<br>(Downtown Portland)</div>
      <div class="venue-address">482 Wexley Street,<br>Portland, ME 04109</div>
    </div>
  </section>

  <footer class="contact-bar">
    <div class="contact-item">
      <span class="contact-icon"><svg width="16" height="16" viewBox="0 0 16 16"><path d="M3 1 L6 4 L4.5 6 C5.5 8 8 10.5 10 11.5 L12 10 L15 13 L13 15 C7 15 1 9 1 3Z" fill="var(--blue)"/></svg></span>
      (207) 555 3184
    </div>
    <div class="contact-item">
      <span class="contact-icon"><svg width="16" height="12" viewBox="0 0 16 12"><rect x="1" y="1" width="14" height="10" rx="1" fill="none" stroke="var(--blue)" stroke-width="2"/><path d="M1 2 L8 7 L15 2" fill="none" stroke="var(--blue)" stroke-width="2"/></svg></span>
      contact@meadowcrest.org
    </div>
    <div class="contact-item">
      <span class="contact-icon"><svg width="18" height="18" viewBox="0 0 18 18" fill="none" stroke="var(--blue)" stroke-width="1.5"><circle cx="9" cy="9" r="7.5"/><ellipse cx="9" cy="9" rx="3.5" ry="7.5"/><path d="M1.5 9 H16.5 M3 5 H15 M3 13 H15"/></svg></span>
      www.vostel.org
    </div>
  </footer>
</main>
</body>
</html>
```